Silver Brook Constructions Ltd Stationary
business cards, stationary etc.
Silver Brook Constructions Ltd Stationary - Construction
Creative Brief
Simple
Dalton Wexford
4816 Ardmore Rd. Harlow Bay B.C. V8N 4K7
250-384-6252 could we put this number under office instead of phone
222-222-2222 temporary until I get new number
dalton@silverbrookconstructions.example
www.silverbrookconstructions.example
We would like designs for business cards , envelopes, letterhead, thank-you cards with evelopes, fax cover sheet, and presentation folder. Thank you
information should be on the back of the card along with some clean lines and simplicity while keeping a very professional feel

```html
<!DOCTYPE html>
<html lang="en">
<head>
<meta charset="utf-8">
<title>Silver Brook Constructions Ltd Stationery</title>
<link href="https://fonts.googleapis.com/css2?family=Cinzel:wght@600&family=Open+Sans:wght@400;600&display=swap" rel="stylesheet">
<style>
  :root {
    --board: #2a2a2a;
    --board-light: #353535;
    --paper: #ffffff;
    --ink: #2b2b2b;
    --muted: #8a8a8a;
    --green-dark: #2f5a1c;
    --green: #5f9a2e;
    --green-light: #a6cf5a;
    --charcoal: #1d1d1d;
    --caption: #9a9a9a;
  }
  * { box-sizing: border-box; margin: 0; padding: 0; }
  html, body { width: 1200px; height: 317px; overflow: hidden; }
  body {
    position: relative;
    background: radial-gradient(ellipse at 50% 40%, var(--board-light), var(--board) 70%);
    font-family: "Open Sans", sans-serif;
    color: var(--ink);
  }
  .piece { position: absolute; background: var(--paper); overflow: hidden; box-shadow: 0 1px 3px rgba(0,0,0,.5); }
  .piece--dark { background: var(--charcoal); color: var(--paper); }
  .caption { position: absolute; font-size: 5px; color: var(--caption); text-align: center; }
  .swoosh { position: absolute; left: 0; top: 0; width: 100%; }
  .wordmark { font-family: "Cinzel", serif; font-weight: 600; color: var(--ink); line-height: 1; white-space: nowrap; }
  .name-dot { border-radius: 50%; background: var(--green); }
  .small { font-size: 4.5px; line-height: 1.45; color: var(--muted); }

  /* name sheet */
  .logo-sheet { left: 8px; top: 10px; width: 92px; height: 96px; display: flex; flex-direction: column; align-items: center; justify-content: center; gap: 8px; }
  .logo-sheet .name-dot { width: 40px; height: 40px; }
  .logo-sheet .wordmark { font-size: 8px; text-align: center; }

  /* business cards */
  .card { width: 86px; height: 44px; }
  .card--a { left: 8px; top: 114px; }
  .card--b { left: 100px; top: 114px; }
  .card--c { left: 8px; top: 166px; }
  .card--d { left: 100px; top: 166px; }
  .card .name-dot { position: absolute; width: 14px; height: 14px; left: 8px; top: 15px; }
  .card--dark-face .wordmark { position: absolute; left: 27px; top: 19px; font-size: 6px; color: var(--paper); }
  .card .person { position: absolute; left: 6px; top: 15px; font-size: 5px; font-weight: 600; }
  .card .contact { position: absolute; left: 6px; top: 22px; font-size: 3.6px; line-height: 1.4; color: var(--muted); }

  /* letterheads */
  .letter { top: 8px; width: 206px; height: 284px; }
  .letter--one { left: 200px; }
  .letter--two { left: 432px; }
  .letter .wordmark { position: absolute; left: 12px; top: 14px; font-size: 7px; }
  .letter .footer { position: absolute; left: 0; bottom: 10px; width: 100%; text-align: center; }

  /* envelopes */
  .envelope { left: 655px; top: 10px; width: 262px; height: 118px; }
  .envelope .wordmark { position: absolute; left: 12px; top: 32px; font-size: 8px; }
  .envelope .return { position: absolute; left: 12px; top: 46px; }
  .thanks-env { left: 665px; top: 188px; width: 200px; height: 96px; }
  .thanks-env .wordmark { position: absolute; left: 10px; top: 26px; font-size: 6px; }
  .thanks-card { left: 874px; top: 168px; width: 78px; height: 96px; }
  .thanks-card .name-dot { position: absolute; left: 26px; top: 34px; width: 26px; height: 26px; }

  /* folder */
  .folder-front { left: 962px; top: 8px; width: 228px; height: 132px; background: linear-gradient(180deg, var(--green-dark), #1f3a14); }
  .folder-front .web { position: absolute; left: 0; width: 100%; top: 86px; text-align: center; font-size: 5px; color: var(--paper); letter-spacing: .08em; }
  .folder-inside { left: 962px; top: 150px; width: 228px; height: 132px; }
  .folder-inside .band { position: absolute; left: 0; top: 54px; width: 100%; height: 16px; background: linear-gradient(90deg, var(--green-dark), var(--green), var(--green-light)); }
  .folder-inside .web { position: absolute; left: 0; width: 100%; top: 59px; text-align: center; font-size: 5px; color: var(--paper); letter-spacing: .08em; }
</style>
</head>
<body>

  <section class="piece logo-sheet">
    <div class="name-dot" aria-hidden="true"></div>
    <div class="wordmark">SILVER BROOK</div>
  </section>

  <section class="piece piece--dark card card--a card--dark-face">
    <div class="name-dot" aria-hidden="true"></div>
    <div class="wordmark">SILVER BROOK</div>
  </section>
  <section class="piece card card--b">
    <svg class="swoosh" viewBox="0 0 86 14" preserveAspectRatio="none" height="12"><path d="M20 0H86V9C60 14 40 4 20 0Z" fill="var(--green)"/></svg>
    <div class="person">Dalton Wexford</div>
    <div class="contact">Office 250-384-6252 · Cell 222-222-2222<br>dalton@silverbrookconstructions.example<br>4816 Ardmore Rd. Harlow Bay B.C. V8N 4K7</div>
  </section>
  <section class="piece piece--dark card card--c card--dark-face">
    <div class="name-dot" aria-hidden="true"></div>
    <div class="wordmark">SILVER BROOK</div>
  </section>
  <section class="piece card card--d">
    <svg class="swoosh" viewBox="0 0 86 14" preserveAspectRatio="none" height="12"><path d="M20 0H86V9C60 14 40 4 20 0Z" fill="var(--green-dark)"/></svg>
    <div class="person">Dalton Wexford</div>
    <div class="contact">Office 250-384-6252 · Cell 222-222-2222<br>www.silverbrookconstructions.example</div>
  </section>
  <div class="caption" style="left:8px;top:213px;width:86px">Card Front</div>
  <div class="caption" style="left:100px;top:213px;width:86px">Card Back</div>

  <section class="piece letter letter--one">
    <svg class="swoosh" viewBox="0 0 206 40" preserveAspectRatio="none" height="40">
      <defs><linearGradient id="lh1" x1="0" x2="1"><stop offset="0" stop-color="var(--green-dark)"/><stop offset="1" stop-color="var(--green-light)"/></linearGradient></defs>
      <path d="M70 0H206V24C160 38 110 14 70 0Z" fill="url(#lh1)"/>
      <path d="M64 0C110 18 160 40 206 30" stroke="var(--green)" stroke-width=".8" fill="none"/>
    </svg>
    <div class="wordmark">SILVER BROOK</div>
    <div class="footer small">4816 Ardmore Rd. Harlow Bay B.C. V8N 4K7 · Office 250-384-6252<br>www.silverbrookconstructions.example</div>
  </section>
  <section class="piece letter letter--two">
    <svg class="swoosh" viewBox="0 0 206 40" preserveAspectRatio="none" height="40">
      <defs><linearGradient id="lh2" x1="0" x2="1"><stop offset="0" stop-color="var(--green-dark)"/><stop offset="1" stop-color="var(--green-light)"/></linearGradient></defs>
      <path d="M0 0H206V20C150 36 70 10 0 26Z" fill="url(#lh2)"/>
    </svg>
    <div class="footer small">dalton@silverbrookconstructions.example · 222-222-2222</div>
  </section>
  <div class="caption" style="left:200px;top:296px;width:206px">Letterhead</div>
  <div class="caption" style="left:432px;top:296px;width:206px">Fax Cover Sheet</div>

  <section class="piece envelope">
    <svg class="swoosh" viewBox="0 0 262 30" preserveAspectRatio="none" height="26">
      <defs><linearGradient id="ev" x1="0" x2="1"><stop offset="0" stop-color="var(--green-dark)"/><stop offset="1" stop-color="var(--green-light)"/></linearGradient></defs>
      <path d="M0 0H262V16C180 30 90 6 0 20Z" fill="url(#ev)"/>
    </svg>
    <div class="wordmark">SILVER BROOK</div>
    <div class="return small">4816 Ardmore Rd.<br>Harlow Bay B.C. V8N 4K7</div>
  </section>
  <div class="caption" style="left:655px;top:131px;width:262px">Envelope</div>

  <section class="piece thanks-env">
    <svg class="swoosh" viewBox="0 0 200 24" preserveAspectRatio="none" height="20">
      <path d="M0 0H200V12C140 24 70 4 0 16Z" fill="var(--green)"/>
    </svg>
    <div class="wordmark">SILVER BROOK</div>
  </section>
  <section class="piece thanks-card">
    <div class="name-dot" aria-hidden="true"></div>
  </section>
  <div class="caption" style="left:665px;top:287px;width:200px">Card Envelope</div>
  <div class="caption" style="left:874px;top:267px;width:78px">Thank-You Card</div>

  <section class="piece folder-front">
    <svg class="swoosh" viewBox="0 0 228 60" preserveAspectRatio="none" height="60">
      <path d="M0 0H228L114 56Z" fill="var(--green)"/>
      <path d="M0 0L114 56L228 0" stroke="var(--green-light)" stroke-width="1" fill="none"/>
    </svg>
    <div class="web">www.silverbrookconstructions.example</div>
  </section>
  <section class="piece folder-inside">
    <div class="band"></div>
    <div class="web">www.silverbrookconstructions.example</div>
  </section>
  <div class="caption" style="left:962px;top:141px;width:228px">Folder Front</div>
  <div class="caption" style="left:962px;top:285px;width:228px">Folder Inside</div>

</body>
</html>
```